Web Design Project GraceHaven - Design+Coding

GraceHaven-Temecula needs a new website! Design + Coding required.

This church is looking for a highly designed, highly interactive web platform from which to launch their ministry.

We're looking for a highly creative web developer that can grasp the vision for this site and take ownership of the development to conceive engaging additional details and elements for the site.

A cookie cutter website template just won't do it for this one. Even though the initial site is not large, it should feel highly designed and highly engaging. In the words of their Senior Pastor: “We want people to realize that if we care this much about a website, imagine how much more we're going care about their family!”

Details: GraceHaven - Temecula is a new church plant in Temecula, CA built on a self-replicating "missionary" model. Essentially, the goal is to attract people, point them to Christ, develop them into mature Christians and send them out to plant churches as part of church plant "teams". This model resembles more of what is done overseas then in the USA.

As well, the Church is what is called "Family Integrated" which means that it ministers to the family as well as the individual. That means children and parents attend services together as a family unit. As such, the site needs to be "family friendly" and welcoming.

The Logo files are attached. They do not need to drive the palette of the site per se but the logo should look like it "belongs" on the site.

Website has 6 main landing pages with limited add'l content pages.

No Flash. Should look good on mobile as well as traditional browser.

Should be "scalable" - easy to expand nav bars, pages, etc as the church grows with ability to add plug ins (like Google maps or iTunes podcast downloads).

PLEASE SEE ATTACHED DOCUMENT: GH-T Website Info.doc for more details.

Logo File attached below.

Use your imagination! Have fun... design a church website that you would want to visit and interact with. If you think of things we might have missed that add great functionality, value, uniqueness or enhance user experience, add them!!! God bless!

-

Another Marigold Studios Inc/Pixel Forum Job. Thanks again Designers!

Industry/Entity Type

Church

Requirements
Must have
• Must be a fully coded, functional website.

Site must be tested and good to go in IE 7+, Firefox 9+, Chrome and both Apple and Android Mobile platforms.

Blog must be one that church can easily upload content to as an integrated part of the site (no Blogger.com, etc plugins please).

Final handover must include full rights to the designs, stock art, coding, etc (so, no "one use templates" please).

Must be a user-scalable platform on a user friendly CMS (CMS is designers choice so long as it is industry standard and user friendly). We want the church to be able to add or modify page elements themselves.

Final handover will include loading and testing on to our hosting server.

The designer must be willing to support the site for 30 days after launch as part of the site payment.
Nice to have
• Prefer a custom designed template (should not look like a "cookie cutter" site).

See attached doc for more!
Should not have
• Any non-standard CMS or industry unsupported plugins.

No Flash.

```html
<!DOCTYPE html>
<html lang="en">
<head>
<meta charset="utf-8">
<title>GraceHaven Temecula Administration</title>
<link href="https://fonts.googleapis.com/css2?family=Arimo:wght@400;700&display=swap" rel="stylesheet">
<style>
:root{
  --ink:#333;
  --link:#1f5a8a;
  --title-blue:#165b8c;
  --band-blue:#1d79b4;
  --line:#ccc;
  --panel:#f4f4f4;
  --row-alt:#f0f0f0;
  --star:#f08c1a;
  --tick:#3a9b2a;
  --muted:#777;
}
*{box-sizing:border-box;margin:0;padding:0}
html,body{width:1200px;height:622px;overflow:hidden;background:#fff;font-family:"Arimo",Arial,sans-serif;color:var(--ink)}
.frame{position:absolute;left:10px;top:10px;width:1180px;height:581px;border:1px solid var(--line);border-radius:8px;overflow:hidden;background:#fff}
.masthead{position:absolute;left:0;top:0;width:100%;height:87px;background:linear-gradient(#2a2a2a,#4a4a4a 45%,#111 85%,#000)}
.masthead h1{position:absolute;left:28px;top:11px;color:#fff;font-size:21px;font-weight:700;letter-spacing:.2px}
.brand-box{position:absolute;left:911px;top:6px;width:264px;height:76px;background:#fff;border:2px solid #bbb;border-radius:6px;display:flex;align-items:center;justify-content:center;gap:10px}
.brand-box .mark{width:18px;height:18px;background:var(--title-blue)}
.brand-box span{font-size:26px;font-weight:700;color:var(--title-blue)}
.band{position:absolute;left:0;top:87px;width:100%;height:16px;background:linear-gradient(var(--band-blue),#135c8e)}
.menubar{position:absolute;left:0;top:106px;width:100%;height:25px;background:linear-gradient(#fafafa,#e6e6e6);border-top:1px solid #ddd;border-bottom:1px solid var(--line);font-size:12px;font-weight:700}
.menubar ul{list-style:none;position:absolute;left:0;top:0;height:100%}
.menubar li{position:absolute;top:0;height:100%;line-height:23px;text-align:center;border-right:1px solid var(--line)}
.status{position:absolute;right:12px;top:0;display:flex;gap:12px;line-height:23px;font-weight:400;font-size:12px}
.status i{display:inline-block;width:11px;height:11px;border-radius:50%;margin-right:5px;vertical-align:-1px}
.status .lnk{color:var(--link)}
.toolbar{position:absolute;left:12px;top:142px;width:1153px;height:68px;background:var(--panel);border:1px solid var(--line);border-radius:8px}
.page-icon{position:absolute;left:12px;top:6px;width:46px;height:48px;border:1px solid #aaa;background:#fff;border-radius:3px}
.page-icon b{position:absolute;left:4px;right:4px;top:4px;height:8px;background:#3d86c6}
.page-icon em{position:absolute;left:4px;right:4px;top:16px;height:14px;background:repeating-linear-gradient(#ccc 0 1px,transparent 1px 3px)}
.page-icon s{position:absolute;left:4px;right:4px;bottom:4px;height:8px;background:repeating-linear-gradient(90deg,#f0a020 0 11px,transparent 11px 14px)}
.toolbar h2{position:absolute;left:74px;top:19px;font-size:21px;color:var(--title-blue);font-weight:700}
.actions{position:absolute;left:755px;top:5px;height:56px}
.actions div{position:absolute;top:0;height:56px;text-align:center;font-size:12px;color:var(--link);white-space:nowrap}
.actions div.sep{border-left:1px solid #ddd}
.actions svg{display:block;margin:4px auto 4px;width:30px;height:30px}
.tabs{position:absolute;left:12px;top:232px;width:1153px;height:27px;border:1px solid var(--line);border-radius:13px;background:linear-gradient(#fff,#f0f0f0);font-size:13px;font-weight:700}
.tabs span{position:absolute;top:5px;padding-right:14px;border-right:1px solid var(--line)}
.tabs .on{left:24px;color:var(--title-blue)}
.tabs .off{left:92px;color:var(--muted)}
.listing{position:absolute;left:12px;top:280px;width:1153px;height:287px;border:1px solid var(--line);border-radius:8px;background:var(--panel)}
.filter{position:absolute;left:22px;top:22px;font-size:12px;display:flex;align-items:center}
.filter input{width:120px;height:17px;border:1px solid #aaa;margin-right:6px}
.filter button{font:14px "Arimo",Arial,sans-serif;height:20px;padding:0 6px;border:1px solid #aaa;background:#fff;margin-right:5px}
.select{position:absolute;top:23px;height:17px;font-size:11px;border:1px solid #aaa;background:#fff;padding:1px 18px 0 4px;white-space:nowrap}
.select svg{position:absolute;right:1px;top:1px;width:13px;height:13px}
.rule{position:absolute;left:10px;right:10px;top:58px;border-top:1px solid #ddd}
table{position:absolute;left:11px;top:70px;width:1128px;border-collapse:collapse;table-layout:fixed;font-size:12px;background:#fff;border-bottom:2px solid #bbb}
th{height:23px;color:var(--title-blue);font-weight:700;border-bottom:1px solid var(--line);border-left:1px solid #fff;background:var(--panel)}
td{height:29.5px;border-left:1px solid #fff;text-align:center;color:#555;font-size:12px}
tbody tr:nth-child(even) td{background:var(--row-alt)}
td.style{text-align:left;color:var(--link)}
td.loc{font-size:11.5px}
td.tpl{text-align:left;font-size:14px;color:var(--link);padding-left:7px}
td.style i{display:inline-block;width:16px;height:13px;border:1px solid #9aa;background:#e8f0f6;margin:0 4px 0 7px;vertical-align:-1px}
.cb{display:inline-block;width:12px;height:12px;border:1px solid #888;background:#fff}
.tick{display:inline-block;width:15px;height:15px;border-radius:50%;background:var(--tick);color:#fff;font-size:10px;line-height:15px;font-weight:700}
.star-on{color:var(--star);font-size:16px}
.star-off{color:#bbb;font-size:16px}
.sort{display:inline-block;width:10px;height:8px;margin-left:3px;background:repeating-linear-gradient(#777 0 1px,transparent 1px 2px)}
.pager{position:absolute;left:0;right:0;top:251px;text-align:center;font-size:12px}
.pager span{position:relative;display:inline-block;height:15px;border:1px solid #aaa;background:#fff;padding:0 22px 0 3px;font-size:11px;vertical-align:-3px}
.pager svg{position:absolute;right:1px;top:0;width:13px;height:13px}
.version{position:absolute;top:597px;left:0;width:100%;text-align:center;font-size:12px}
</style>
</head>
<body>
<div class="frame">
  <header class="masthead">
    <h1>GraceHaven Temecula Administration</h1>
    <div class="brand-box"><i class="mark"></i><span>GraceHaven</span></div>
  </header>
  <div class="band"></div>
  <nav class="menubar">
    <ul>
      <li style="left:0;width:50px">Site</li>
      <li style="left:50px;width:58px">Users</li>
      <li style="left:108px;width:62px">Menus</li>
      <li style="left:170px;width:67px">Content</li>
      <li style="left:237px;width:98px">Components</li>
      <li style="left:335px;width:86px">Extensions</li>
      <li style="left:421px;width:52px">Help</li>
    </ul>
    <div class="status">
      <span><i style="background:#e0a030"></i>0 Visitors</span>
      <span><i style="background:#3a7cc0"></i>1 Admin</span>
      <span><i style="background:#888"></i>0</span>
      <span class="lnk"><i style="background:#3a7cc0;border-radius:0;width:14px"></i>View Site</span>
      <span class="lnk"><i style="background:#d33"></i>Log out</span>
    </div>
  </nav>
  <section class="toolbar">
    <div class="page-icon"><b></b><em></em><s></s></div>
    <h2>Template Manager: Styles</h2>
    <div class="actions">
      <div style="left:0;width:110px"><svg viewBox="0 0 30 30"><polygon points="15,2 19,11 28,11 21,17 24,27 15,21 6,27 9,17 2,11 11,11" fill="#f29a1f"/></svg>Make Default</div>
      <div class="sep" style="left:104px;width:52px"><svg viewBox="0 0 30 30"><circle cx="15" cy="15" r="13" fill="#2a7bc4"/><path d="M9 21l2-5 8-8 3 3-8 8z" fill="#f3c64a"/></svg>Edit</div>
      <div style="left:156px;width:66px"><svg viewBox="0 0 30 30"><rect x="5" y="3" width="16" height="20" fill="#eee" stroke="#999"/><rect x="9" y="7" width="16" height="20" fill="#fff" stroke="#999"/></svg>Duplicate</div>
      <div class="sep" style="left:230px;width:58px"><svg viewBox="0 0 30 30"><rect x="7" y="4" width="16" height="4" fill="#3a8fd0"/><path d="M8 9h14l-2 18H10z" fill="#3a8fd0"/><circle cx="22" cy="22" r="5" fill="#d22"/><rect x="19" y="21" width="6" height="2" fill="#fff"/></svg>Delete</div>
      <div class="sep" style="left:289px;width:66px"><svg viewBox="0 0 30 30"><rect x="3" y="3" width="24" height="24" rx="3" fill="#ddd" stroke="#777"/><text x="8" y="20" font-size="11" font-family="Arimo,Arial,sans-serif" fill="#333">AB</text></svg>Options</div>
      <div class="sep" style="left:355px;width:56px"><svg viewBox="0 0 30 30"><circle cx="15" cy="15" r="12" fill="none" stroke="#e2552b" stroke-width="6" stroke-dasharray="9 3.5"/></svg>Help</div>
    </div>
  </section>
  <div class="tabs"><span class="on">Styles</span><span class="off">Templates</span></div>
  <section class="listing">
    <div class="filter">Filter:<input type="text"><button>Search</button><button>Clear</button></div>
    <div class="select" style="left:898px">- Select Template -<svg viewBox="0 0 13 13"><rect x=".5" y=".5" width="12" height="12" fill="#e6e6e6" stroke="#777"/><path d="M3.5 5h6l-3 4z" fill="#222"/></svg></div>
    <div class="select" style="left:1019px">- Select Location -<svg viewBox="0 0 13 13"><rect x=".5" y=".5" width="12" height="12" fill="#e6e6e6" stroke="#777"/><path d="M3.5 5h6l-3 4z" fill="#222"/></svg></div>
    <div class="rule"></div>
    <table>
      <colgroup><col style="width:35px"><col style="width:600px"><col style="width:115px"><col style="width:235px"><col style="width:53px"><col style="width:62px"><col style="width:28px"></colgroup>
      <thead><tr><th></th><th>Style</th><th>Location</th><th>Template<i class="sort"></i></th><th>Default</th><th>Assigned</th><th>ID</th></tr></thead>
      <tbody>
        <tr><td><span class="cb"></span></td><td class="style"><i></i>Slatewing - Default</td><td class="loc">Administrator</td><td class="tpl">Slatewing</td><td class="star-on">★</td><td></td><td>2</td></tr>
        <tr><td><span class="cb"></span></td><td class="style"><i></i>GraceHaven Temecula Template (blue)</td><td class="loc">Site</td><td class="tpl">Grace_haven</td><td class="star-off">☆</td><td><span class="tick">✓</span></td><td>24</td></tr>
        <tr><td><span class="cb"></span></td><td class="style"><i></i>GraceHaven Temecula Template (violet)</td><td class="loc">Site</td><td class="tpl">Grace_haven</td><td class="star-off">☆</td><td><span class="tick">✓</span></td><td>25</td></tr>
        <tr><td><span class="cb"></span></td><td class="style"><i></i>GraceHaven Temecula Template (green)</td><td class="loc">Site</td><td class="tpl">Grace_haven</td><td class="star-off">☆</td><td><span class="tick">✓</span></td><td>23</td></tr>
        <tr><td><span class="cb"></span></td><td class="style"><i></i>GraceHaven Temecula Template</td><td class="loc">Site</td><td class="tpl">Grace_haven</td><td class="star-on">★</td><td></td><td>22</td></tr>
      </tbody>
    </table>
    <div class="pager">Display # <span>100<svg viewBox="0 0 13 13"><rect x=".5" y=".5" width="12" height="12" fill="#e6e6e6" stroke="#777"/><path d="M3.5 5h6l-3 4z" fill="#222"/></svg></span></div>
  </section>
</div>
<p class="version">Tessera 2.5.8</p>
</body>
</html>
```